Business Card Design - Furniture Retail

Open to both Single or double sided design

We are launching a online ecommerce store that sells Scandinavian/Danish style of furniture in Australia.

We aspire to provide stylish but classic and designers' selection of furniture to the Australia public at affordable price. For the style of the furniture we are selling, please see the following links:

https://www.boxlyshare.com/sh/qrk7vz2mwpl04tn/BBXTpeLr3h52Kd7nWqYzRsGmu?dl=0

The style of the design we are looking for is clean, simple that look Scandinavian/Danish but yet it is timeless classic.

Aspiring Design
http://www.hallwick.com
http://brenlowe.com.au/
http://kolvo.furniture/
http://www.tipo.com/
Updates

Please display the card on normal angle for both front and back instead of funny angle. Please keep it display when displaying the design of the business cards so that we can focus on the designs rather than being confused by the unnecessary stuffs like the hands or background

I think there is already enough curve line on the logo itself so anything extra of the curve on the business card would be really unnecessary. Please avoid using any of the extra curve line on the business card, other than the logo itself. Thanks

Regular card and give them a matt celloglaze to create texture on card that makes it looked luxury and expensive.

Please display design on normal angle! Please only use white colour in the background (not the business card but the referring to the submission) rather than anything fancy so that we can focus on the design.

Target Market(s)

High end market consumers who are financially capable and who has good taste and appreciate good design

aged between 28 - 45 white collars professional/businessmen who live in metropolitan areas

Industry/Entity Type

Business

Font styles to use
Serif
Sans Serif

Requirements
Must have
• Regular card and give them a matt celloglaze to create texture on card that makes it looked luxury and expensive.

Please use the logo from the uploaded files

Company Name: Miles Orveda
Name: Peter Holm
Phone: +614 27 505 316
Website: www.milesorveda.com.au
Email: peter@milesorveda.com.au
Nice to have
• Colour is not limited to black and white
Should not have
• The concept photos of the furniture should NOT be used in the FRONT page of the business card.

```html
<!DOCTYPE html>
<html lang="en">
<head>
<meta charset="utf-8">
<title>Miles Orveda — Business Card</title>
<link rel="stylesheet" href="https://fonts.googleapis.com/css2?family=Noto+Serif&display=swap">
<style>
  :root {
    --page-bg: #ffffff;
    --card-white: #ffffff;
    --card-shade: #dcdcdc;
    --ink: #1c1b1b;
    --rule: #3a3a3a;
    --band: #232122;
    --band-text: #f4f4f4;
  }
  * { box-sizing: border-box; margin: 0; padding: 0; }
  html, body {
    width: 1200px; height: 1200px; overflow: hidden;
    background: var(--page-bg);
    font-family: "Noto Serif", Georgia, serif;
    color: var(--ink);
  }
  .sheet {
    width: 1200px; height: 1200px;
    display: flex; flex-direction: column; align-items: center; justify-content: center;
    gap: 60px;
  }
  .card {
    position: relative;
    width: 860px; height: 491px;
    background: radial-gradient(ellipse at 60% 65%, var(--card-white) 35%, var(--card-shade) 100%);
    box-shadow: 0 2px 10px rgba(0,0,0,0.18);
    overflow: hidden;
  }
  .card__wordmark {
    position: absolute;
    font-size: 64px; letter-spacing: 4px;
    text-transform: uppercase; white-space: nowrap;
  }
  .card__rule {
    position: absolute; left: 0; right: 0; height: 2px;
    background: var(--rule);
  }
  .card__name {
    position: absolute; font-size: 30px; white-space: nowrap;
  }
  .card__contacts {
    position: absolute; left: 60px;
    list-style: none; font-size: 27px;
  }
  .card__contacts li {
    display: flex; align-items: center; gap: 16px; margin-bottom: 18px;
  }
  .card__contacts svg { width: 22px; height: 22px; fill: var(--ink); flex: none; }
  .card__band {
    position: absolute; left: 0; right: 0; bottom: 0; height: 108px;
    background: var(--band);
    display: flex; align-items: flex-end; justify-content: center;
    padding-bottom: 22px;
    color: var(--band-text); font-size: 27px; letter-spacing: 0.5px;
  }

  /* front variant */
  .card--front .card__wordmark { left: 56px; top: 96px; }
  .card--front .card__rule { top: 210px; }
  .card--front .card__name { right: 72px; top: 238px; }
  .card--front .card__contacts { top: 290px; }

  /* alternate variant */
  .card--alt .card__wordmark { right: 56px; top: 60px; }
  .card--alt .card__rule { top: 190px; }
  .card--alt .card__name { right: 72px; top: 230px; }
  .card--alt .card__contacts { top: 222px; }
</style>
</head>
<body>
<main class="sheet">

  <section class="card card--front" aria-label="Business card, front">
    <h1 class="card__wordmark">Miles Orveda</h1>
    <div class="card__rule"></div>
    <p class="card__name">Peter Holm</p>
    <ul class="card__contacts">
      <li>
        <svg viewBox="0 0 24 24" aria-hidden="true"><path d="M6.6 10.8a15.1 15.1 0 0 0 6.6 6.6l2.2-2.2a1 1 0 0 1 1-.25 11.4 11.4 0 0 0 3.6.57 1 1 0 0 1 1 1V20a1 1 0 0 1-1 1A17 17 0 0 1 3 4a1 1 0 0 1 1-1h3.5a1 1 0 0 1 1 1c0 1.25.2 2.45.57 3.57a1 1 0 0 1-.25 1z"/></svg>
        <span>+614 27 505 316</span>
      </li>
      <li>
        <svg viewBox="0 0 24 24" aria-hidden="true"><path d="M2 6h20v2.2l-10 6-10-6z M2 10.5l10 6 10-6V19H2z"/></svg>
        <span>peter@milesorveda.com.au</span>
      </li>
    </ul>
    <footer class="card__band">www.milesorveda.com.au</footer>
  </section>

  <section class="card card--alt" aria-label="Business card, alternate layout">
    <h2 class="card__wordmark">Miles Orveda</h2>
    <div class="card__rule"></div>
    <p class="card__name">Peter Holm</p>
    <ul class="card__contacts">
      <li><span>+614 27 505 316</span></li>
      <li><span>peter@milesorveda.com.au</span></li>
    </ul>
    <footer class="card__band">www.milesorveda.com.au</footer>
  </section>

</main>
</body>
</html>
```